Brochure Design Project

I would like for it took look a little different than my website, elegant, and classy. Our company wants to draw upper class customers to care for their home. We also focus private water taxi services for businesses to taxi their employees.

Target Market(s)

tourists, seasonal residents, property management.

Industry/Entity Type

Professional Service

Font styles to use
Serif

Requirements
Must have
• 2 sides

```html
<!DOCTYPE html>
<html lang="en">
<head>
<meta charset="utf-8">
<title>Harborlight Concierge Services – Brochure</title>
<link href="https://fonts.googleapis.com/css2?family=Source+Sans+3:wght@400;600;700&family=Cinzel:wght@500&family=Bebas+Neue&display=swap" rel="stylesheet">
<style>
  :root{
    --backdrop:#4a4a4a;
    --frame:#8b4a22;
    --frame-dark:#6e3716;
    --paper:#ece2cc;
    --paper-edge:#ddcfb2;
    --rust:#b35f2b;
    --rust-box:#b0612f;
    --ink:#1d1a17;
    --logo-bg:#3d302a;
    --bar:#2a2a2a;
    --white:#ffffff;
  }
  *{box-sizing:border-box;margin:0;padding:0}
  html,body{width:1200px;height:1200px;overflow:hidden}
  body{background:var(--backdrop);position:relative;font-family:"Source Sans 3",sans-serif;color:var(--ink)}
  .brochure{position:absolute;left:30px;top:156px;width:1140px;height:887px;background:linear-gradient(135deg,var(--frame),var(--frame-dark))}
  .panel{position:absolute;top:25px;height:838px;background:radial-gradient(ellipse at 40% 30%,var(--paper) 55%,var(--paper-edge) 100%)}
  .panel--about{left:23px;width:340px}
  .panel--contact{left:389px;width:351px}
  .panel--cover{left:763px;width:351px;top:26px}
  .abs{position:absolute}
  .label{position:absolute;left:12px;background:#f6f1e6;color:var(--rust);font-weight:700;font-size:15.5px;padding:1px 12px 1px 5px;letter-spacing:.2px;box-shadow:1px 1px 2px rgba(0,0,0,.15)}
  .body-text{position:absolute;left:14px;right:11px;font-size:13.3px;line-height:16.8px;text-align:justify;hyphens:auto}
  .rule{position:absolute;height:1px;background:var(--ink)}
  .call-lead{left:0;right:0;text-align:center;top:43px;font-size:18.5px}
  .call-number{left:0;right:0;text-align:center;top:64px;font-size:32px;font-weight:700;color:var(--rust);letter-spacing:.5px}
  .call-strong{left:15px;right:16px;font-size:13.3px;font-weight:700;line-height:16.8px}
  .contact-card{position:absolute;left:20px;top:481px;width:308px;height:244px;border:2px solid var(--rust);display:flex;flex-direction:column;align-items:center;justify-content:center;gap:4px;font-size:13.3px;font-style:normal}
  .contact-card svg{display:block}
  .contact-item{display:flex;flex-direction:column;align-items:center;gap:5px;margin-bottom:6px}
  .cover-photo{position:absolute;left:0;top:0;width:351px;height:314px;background:linear-gradient(160deg,#e9eef2 0%,#c8d4de 45%,#6d7a88 75%,#3f4650 100%)}
  .brand{position:absolute;left:86px;top:0;width:181px;height:137px;background:var(--logo-bg);color:var(--white);display:flex;flex-direction:column;align-items:center;justify-content:center;gap:8px;font-size:12px;letter-spacing:1.2px;text-align:center;line-height:21px;padding-top:22px}
  .brand-dot{width:18px;height:18px;border:1.5px solid var(--white);border-radius:50%;margin-bottom:4px}
  .headline{position:absolute;left:22px;top:348px;width:308px;height:190px;background:var(--rust-box);color:var(--white);padding:12px 10px 0 14px;font-weight:normal;overflow:hidden}
  .headline-serif{display:block;font-family:"Cinzel",serif;font-weight:500;font-size:31px;line-height:42px;white-space:nowrap}
  .headline-serif .big{font-size:45px}
  .headline-bold{display:block;font-family:"Bebas Neue",sans-serif;font-size:70px;line-height:74px;letter-spacing:0;white-space:nowrap}
  .promise{position:absolute;left:22px;top:576px;width:308px;height:190px;border:2px solid var(--rust);padding:34px 10px 0 11px;font-size:15.5px;line-height:20.2px;text-align:justify;hyphens:auto}
  .site-bar{position:absolute;left:0;top:799px;width:351px;height:21px;background:var(--bar);color:var(--white);text-align:center;font-size:13px;line-height:21px;letter-spacing:2px}
</style>
</head>
<body>
<main class="brochure">

  <section class="panel panel--about">
    <h2 class="label" style="top:50px">ABOUT US</h2>
    <p class="body-text" style="top:95px">Founded in 2017 by Daniel and Claire Whitmore, Harborlight Concierge provides the Pine Island area with an exclusive list of services for property management including home services, rental guest liaison, and tailored concierge services. We are also offer private charters for water transportation to barrier islands, exclusive fishing adventures, and sightseeing tours.</p>

    <h2 class="label" style="top:224px">CLAIRE WHITMORE</h2>
    <p class="body-text" style="top:268px">As co-owner and operator of Harborlight Concierge, Claire combines her strong professional background in healthcare with a passion in caring for people in the community. Born and raised in Florida, Claire graduated from a local university with a Bachelor’s Degree in Science Nursing. With years of business experience within the largest healthcare system in the state, she has held extraordinary positions that involve utilization management and centralized solutions. During her free time she enjoys fishing, and boating with her family.</p>

    <h2 class="label" style="top:481px">DANIEL WHITMORE</h2>
    <p class="body-text" style="top:528px">With a strong corporate background and well-known experience working with one of the largest power and energy companies in the world, Daniel knows the importance of providing top level customer service. Also born and raised in Florida, Daniel completed an apprenticeship program in Miami where he earned his title as a Line Specialist. Now retired, throughout the years he continued to peruse his passion for competitive sports fishing where he developed long standing professional relationships within his community.</p>

    <div class="rule" style="left:72px;width:191px;top:767px"></div>
  </section>

  <section class="panel panel--contact">
    <p class="abs call-lead">Call &amp; speak with a concierge specialist</p>
    <p class="abs call-number">(239) 555-0148</p>
    <p class="abs call-strong" style="top:143px">Concierge services have grown far beyond that of a hotel lobby.</p>
    <p class="abs call-strong" style="top:185px">Call us with your request and HCS will do the rest!</p>
    <p class="body-text" style="top:240px;left:18px;right:18px">Serving Bokeelia and surrounding sister islands, Harborlight concierge is the top innovator in the concierge service industry. Our company has the knowledge and resources through a trusted network of service providers to meet individual needs and preferences for our clients.</p>
    <div class="rule" style="left:76px;width:193px;top:368px"></div>

    <address class="contact-card">
      <div class="contact-item">
        <svg width="20" height="26" viewBox="0 0 20 26" aria-hidden="true"><path d="M10 1a9 9 0 0 0-9 9c0 6.5 9 15 9 15s9-8.5 9-15a9 9 0 0 0-9-9z" fill="var(--rust)"/><circle cx="10" cy="10" r="3.5" fill="var(--paper)"/></svg>
        <span>418 Palmetto Cove Rd Bayhaven Fl 33900</span>
      </div>
      <div class="contact-item">
        <svg width="22" height="20" viewBox="0 0 24 24" aria-hidden="true"><path d="M6.6 10.8a15.1 15.1 0 0 0 6.6 6.6l2.2-2.2a1 1 0 0 1 1-.25 11.4 11.4 0 0 0 3.6.57 1 1 0 0 1 1 1V20a1 1 0 0 1-1 1A17 17 0 0 1 3 4a1 1 0 0 1 1-1h3.5a1 1 0 0 1 1 1c0 1.25.2 2.45.57 3.57a1 1 0 0 1-.25 1z" fill="var(--rust)"/></svg>
        <span>(239) 555-0148</span>
      </div>
      <div class="contact-item">
        <svg width="26" height="18" viewBox="0 0 26 18" aria-hidden="true"><rect x="0" y="0" width="26" height="18" rx="2" fill="var(--rust)"/><path d="M1 1.5l12 9 12-9" fill="none" stroke="var(--paper)" stroke-width="1.6"/></svg>
        <span>HCSatYourService@gmail.com</span>
      </div>
      <div class="contact-item">
        <svg width="24" height="24" viewBox="0 0 24 24" aria-hidden="true"><g fill="none" stroke="var(--rust)" stroke-width="2"><circle cx="12" cy="12" r="10"/><ellipse cx="12" cy="12" rx="4.5" ry="10"/><path d="M2 12h20M4 6.5h16M4 17.5h16"/></g></svg>
        <span>www.hcsatyourservice.com</span>
      </div>
    </address>
  </section>

  <section class="panel panel--cover">
    <div class="cover-photo" role="img" aria-label="Photo of a hand in a blue sleeve ringing a silver service bell on a marble reception desk"></div>
    <div class="brand">
      <span class="brand-dot"></span>
      <span>HARBORLIGHT CONCIERGE<br>SERVICES L.L.C.</span>
    </div>
    <h1 class="headline">
      <span class="headline-serif"><span class="big">Y</span>OUR</span>
      <span class="headline-serif"><span class="big">R</span>EQUEST IS</span>
      <span class="headline-bold">OUR DEMAND</span>
    </h1>
    <p class="promise">Our concierge services are tailored to each request ensuring an exceptional client experience. We have the knowledge and resources through our trusted network of service providers to meet individual needs and preferences.</p>
    <p class="site-bar">www.hcsatyourservice.com</p>
  </section>

</main>
</body>
</html>
```